Web Site Design for a Finance (lending) Company

We are opening a new subsidiary that focuses on lending money in the real estate industry. We need a web site designed to represent the business.

The business is lending money to real estate investors. A typical client/borrower will be looking to borrow money to buy a house, renovate it and then sell it at a profit, all within 12 months or less.

Company name is Brevand Finance. Our logo is attached.

Attached is a general outline for the web site. We're working on writing more text for each page but this should give you enough to get started with some ideas.

Competitor web site that I like a lot (as an example): https://quorvelfunding.com/. Many of the general items on this site match what we will need (description of loan programs, FAQ)

Target Market(s)

Real estate investors (generally individuals or small companies with just a few people) who are buying homes, renovating them and then selling them at a profit.

Industry/Entity Type

Finance

Coding

Coded - Design and coding required

Number of Pages Required

5+ page

Colors

Designer to choose colors to be used in the design.

Requirements
Must have
• Minimalist design. Clean lines without too much clutter. Some stock photography is ok but the photos should not be distracting. They should almost fade in to the background so that user can focus on the key information about what our company does instead. We are a finance company, not a design company, so the information about our products will be more interesting to site visitors than the art.
• Some minimalist examples from Snapboard:
• https://www.snapboard-example.com/explore/minimalist-web-design/
Nice to have
• If you search in seekly for "hard money lenders" you will find many examples of web sites from our competition. I have provided a link above to competitor web site that I like a lot.
• I have attached our logo in EPS format. Logo is green. Web site doesn't have to be green but it should be of a color that will work well with the logo.

```html
<!DOCTYPE html>
<html lang="en">
<head>
<meta charset="utf-8">
<title>Brevand Finance</title>
<link href="https://fonts.googleapis.com/css2?family=Montserrat:wght@400;500;600;700&family=Open+Sans:wght@400;600;700&display=swap" rel="stylesheet">
<style>
:root{
  --green:#1f7a4a;
  --green-dark:#0f4d2c;
  --green-mid:#2f7d55;
  --grey-text:#666;
  --grey-light:#e8e9e8;
  --hero:#7d817f;
  --white:#fff;
  --ink:#333;
}
*{box-sizing:border-box;margin:0;padding:0}
html,body{width:819px;height:1200px;overflow:hidden;background:var(--white);font-family:"Open Sans",sans-serif;color:var(--ink)}
.page{position:relative;width:819px;height:1200px}
.abs{position:absolute}
/* header */
.brand{left:52px;top:26px;display:flex;align-items:center;gap:8px}
.brand-mark{width:14px;height:14px;background:var(--green)}
.brand-name{font-family:"Montserrat",sans-serif;font-weight:600;font-size:14px;color:var(--green-dark)}
.nav{left:192px;top:44px;display:flex;gap:27px;font-family:"Montserrat",sans-serif;font-weight:500;font-size:9.5px;color:#333;letter-spacing:.3px}
.phone{right:60px;top:8px;display:flex;align-items:center;gap:8px;font-family:"Roboto","Open Sans",sans-serif;font-size:10px;color:#666}
.login{left:704px;top:38px;width:62px;height:20px;background:var(--green-dark);color:#fff;font-family:"Montserrat",sans-serif;font-weight:600;font-size:9px;display:flex;align-items:center;justify-content:center}
/* hero */
.hero{left:0;top:70px;width:819px;height:223px;background:linear-gradient(100deg,#8a8d8b 0%,#6f7371 45%,#7a7f7b 70%,#5d6a62 100%)}
.hero-title{left:0;width:819px;top:130px;text-align:center;font-family:"Montserrat",sans-serif;font-size:27px;color:#fff;font-weight:400}
.hero-title b{font-weight:600}
.hero-sub{left:0;width:819px;top:167px;text-align:center;font-family:"Montserrat",sans-serif;font-size:18.5px;line-height:20px;letter-spacing:2.4px;color:#fff;font-weight:500}
.btn{background:var(--green);color:#fff;display:flex;align-items:center;justify-content:center;font-weight:700}
.hero-btn{left:330px;top:227px;width:126px;height:28px;font-family:"Montserrat",sans-serif;font-size:12px;font-weight:600}
/* cards */
.card{top:305px;width:233px;height:167px;background:var(--grey-light)}
.card.primary{background:var(--green-mid)}
.card-art{left:78px;top:17px;width:78px;height:58px;background:#d7dcd9}
.card-text{left:16px;top:85px;width:210px;font-size:9.2px;line-height:14.6px;font-weight:600;color:#555}
.card.primary .card-text{color:#fff}
.card-btn{top:449px;width:103px;height:30px;font-size:9.5px}
.card-btn.light{background:var(--grey-light);color:var(--green)}
/* why */
.why-title{left:0;width:819px;top:530px;text-align:center;font-size:21px;font-weight:600;color:#777}
.why-title b{color:var(--green-dark);font-weight:700}
.why-photo{left:50px;top:589px;width:358px;height:217px;background:linear-gradient(135deg,#f4f1ee 0%,#ecd9c8 45%,#f6f3f1 100%);border:1px solid #eee}
.checks{left:465px;top:590px;list-style:none}
.checks li{display:flex;align-items:center;height:29.4px;font-size:14px;font-weight:600;letter-spacing:1.8px;color:var(--green)}
.checks svg{margin-right:24px}
.apply{left:506px;top:779px;width:219px;height:28px;background:var(--green-dark);font-size:14px;letter-spacing:1.6px;font-weight:600}
.side-bar{left:811px;top:569px;width:8px;height:220px;background:var(--green-mid)}
/* testimonial */
.band{left:0;top:842px;width:819px;height:220px;background:linear-gradient(90deg,#5a4a3a 0%,#6f6a62 40%,#66625b 70%,#574a3d 100%)}
.band::after{content:"";position:absolute;inset:0;background:rgba(40,40,40,.35)}
.band-title{left:0;width:819px;top:894px;text-align:center;font-size:22px;font-weight:700;letter-spacing:2.6px;color:#fff}
.quote{left:60px;width:700px;top:948px;text-align:center;font-size:10.8px;line-height:20px;letter-spacing:.4px;color:#fff}
.author{left:0;width:819px;top:996px;text-align:center;font-size:12px;font-weight:700;letter-spacing:2px;color:#fff}
/* footer */
.foot-h{top:1097px;font-size:16px;letter-spacing:1.6px;color:#555;font-weight:400}
.foot-list{top:1140px;font-size:10.5px;line-height:14.6px;letter-spacing:.8px;color:#777}
.join{left:442px;top:1101px;width:165px;height:39px;background:var(--green-dark);font-size:11px;letter-spacing:.6px;border-radius:2px}
.copy{left:439px;top:1159px;font-size:10.5px;letter-spacing:.8px;color:#777}
.foot-brand{left:676px;top:1112px;display:flex;align-items:center;gap:8px}
.bottom-line{left:0;top:1196px;width:819px;height:4px;background:linear-gradient(90deg,var(--green-dark) 0 54%,#999 54% 100%)}
</style>
</head>
<body>
<div class="page">
  <header>
    <div class="abs brand"><span class="brand-mark"></span><span class="brand-name">Brevand Finance</span></div>
    <nav class="abs nav"><span>HOME</span><span>ABOUT US</span><span>LOANS</span><span>RESOURCES</span><span>CONTACT US</span></nav>
    <div class="abs phone">
      <svg width="18" height="14" viewBox="0 0 18 14"><path d="M2 5c3-4 11-4 14 0l-2 2-2-1V4c-2-1-4-1-6 0v2l-2 1z" fill="#555"/><circle cx="9" cy="8" r="3.5" fill="none" stroke="#555"/></svg>
      <span>1 (800) 555-0147</span>
    </div>
    <div class="abs login">LOGIN</div>
  </header>

  <section>
    <div class="abs hero" role="img" aria-label="Muted photo of small model houses with one green house"></div>
    <h1 class="abs hero-title"><b>BREVAND</b> FINANCE</h1>
    <p class="abs hero-sub">Local real estate experts lending to<br>local real estate investors</p>
    <div class="abs btn hero-btn">Learn More</div>
  </section>

  <section>
    <div class="abs card primary" style="left:50px">
      <p class="abs card-text" style="color:#fff">Brevand Finance is a local business with local knowledge and strong industry relation-ships.</p>
    </div>
    <div class="abs card" style="left:292px">
      <div class="abs card-art" role="img" aria-label="Icon of a house with a dollar sign"></div>
      <p class="abs card-text" style="left:10px">Brevand has an established pool of experienced investors available for your real estate investment needs</p>
    </div>
    <div class="abs card" style="left:534px">
      <div class="abs card-art" style="left:45px;top:15px;width:140px;height:60px" role="img" aria-label="Fix and flip program lettering"></div>
      <p class="abs card-text" style="left:20px">Short Term Financing for the Purchase and Rehab of Single-Family Properties</p>
    </div>
    <div class="abs btn card-btn light" style="left:109px">Read More</div>
    <div class="abs btn card-btn" style="left:354px">Read More</div>
    <div class="abs btn card-btn" style="left:591px">Read More</div>
  </section>

  <section>
    <h2 class="abs why-title">WHY BORROW FROM <b>BREVAND</b></h2>
    <div class="abs why-photo" role="img" aria-label="Photo of a hand dropping coins into an open palm"></div>
    <ul class="abs checks">
      <li><svg width="18" height="15" viewBox="0 0 18 15"><rect x="1" y="3" width="11" height="11" rx="2" fill="none" stroke="#222" stroke-width="2"/><path d="M4 8l3 3 9-10" fill="none" stroke="#222" stroke-width="2.4"/></svg>Experts</li>
      <li><svg width="18" height="15" viewBox="0 0 18 15"><rect x="1" y="3" width="11" height="11" rx="2" fill="none" stroke="#222" stroke-width="2"/><path d="M4 8l3 3 9-10" fill="none" stroke="#222" stroke-width="2.4"/></svg>Fast approval</li>
      <li><svg width="18" height="15" viewBox="0 0 18 15"><rect x="1" y="3" width="11" height="11" rx="2" fill="none" stroke="#222" stroke-width="2"/><path d="M4 8l3 3 9-10" fill="none" stroke="#222" stroke-width="2.4"/></svg>Professional</li>
      <li><svg width="18" height="15" viewBox="0 0 18 15"><rect x="1" y="3" width="11" height="11" rx="2" fill="none" stroke="#222" stroke-width="2"/><path d="M4 8l3 3 9-10" fill="none" stroke="#222" stroke-width="2.4"/></svg>Selective</li>
      <li><svg width="18" height="15" viewBox="0 0 18 15"><rect x="1" y="3" width="11" height="11" rx="2" fill="none" stroke="#222" stroke-width="2"/><path d="M4 8l3 3 9-10" fill="none" stroke="#222" stroke-width="2.4"/></svg>A partner</li>
      <li><svg width="18" height="15" viewBox="0 0 18 15"><rect x="1" y="3" width="11" height="11" rx="2" fill="none" stroke="#222" stroke-width="2"/><path d="M4 8l3 3 9-10" fill="none" stroke="#222" stroke-width="2.4"/></svg>Competitive Rates and Fees</li>
    </ul>
    <div class="abs btn apply">Apply Now</div>
    <div class="abs side-bar"></div>
  </section>

  <section>
    <div class="abs band" role="img" aria-label="Darkened photo of a row of townhouse doors with potted trees"></div>
    <h2 class="abs band-title">See What Our Clients Have to Say</h2>
    <p class="abs quote">“ Quorvel Funding is a great company to work with for investment lending. I loved that I had one main point of contact throughout the process and everything ended up going very smoothly. ”</p>
    <p class="abs author">Daniel R.</p>
  </section>

  <footer>
    <h3 class="abs foot-h" style="left:51px">CONTACT US</h3>
    <p class="abs foot-list" style="left:51px">418 Alderwick Ave.<br>Suite 300<br>Marlow Falls, SC 29000</p>
    <h3 class="abs foot-h" style="left:251px">QUICKLINKS</h3>
    <p class="abs foot-list" style="left:251px">Disclaimer<br>NMLS Consumer Access<br>Customer Portal</p>
    <div class="abs btn join">Join Our Email List</div>
    <p class="abs copy">© 2017&nbsp; Brevand Finance</p>
    <div class="abs foot-brand"><span class="brand-mark"></span><span class="brand-name">Brevand Finance</span></div>
    <div class="abs bottom-line"></div>
  </footer>
</div>
</body>
</html>
```